New Website for Asia Travel Agency

Lanternpath Journeys Website

We want a redesign for our current website, www.lanternpathjourneys.example. We want you to get creative with our brand and present our company in a unique, creative and compelling way, that communicates our exotic destinations and tours, the local and authentic character of our travel consultants and the trustworthy and professional nature of our company.

Who is this company?

Lanternpath Journeys is an online tour operator specializing in providing tailor-made tours to eight destinations in Asia; Vietnam, Thailand, Laos, Cambodia, Indonesia, Myanmar, Japan and China. They were launched in mid February 2012 with headquarters in Bangkok, Thailand, and staffed by locals and expats with many years of experience in the travel industry, and who are committed to sharing their deep knowledge of, and passion for the region.

Local knowledge

Our consultants at Lanternpath Journeys are all locals – they know their destinations inside-out and draw upon invaluable first-hand experience and information when planning your tour. They have insights into local culture and tradition, they know the best places to visit, the most worthwhile experiences to have and, most importantly, they have the knowledge to create exactly the holiday you desire.

All hotels and activities featured in a Lanternpath Journeys tour are regularly inspected by our consultants to ensure the highest quality standards are met and that all information is correct and up to date.

Unforgettable Travel Experiences

Whether it's a cultural exploration or a beach holiday you're after – or a mix of both – Lanternpath Journeys has an itinerary for you – and if we don't have one, we'll tailor-make one! From the main sights to remote villages, our locally based Travel Specialists will give you unique insights into every place you visit and let you delve into known destinations from new perspectives.

Our tours offer a variety of hotel and resort options, premium stays in deluxe accommodation, heritage hotels, a five-star boutique or on the water in a junk. Tap into our experience let us create an experience unique to you – and one you will never forget.

What type of Holiday to Asia?

Our itineraries at Lanternpath Journeys are created according to different inspirations. Some travelers are interested in the History & Culture of a destination, while some like to stay active with Adventure tours. A Cross Border trip explores different countries in a single tour, while Velvet Summit tours offer the highest level of exclusivity across our destinations. There are 14 different Holiday Types to choose from, or you can mix and match ideas to create your dream vacation.

Target Market(s)

Slightly more female, aged 30-65, are creative, professional and looking for something different, something a bit unusual.

Industry/Entity Type

Boutique

Requirements
Must have
• 5 page designs:

1. Homepage
2. Tours list page for a country
3. Tour page
4. 'Be Inspired' page
5. Country page
6. Enquiry page

Our inspirations.

The following list shows websites we love and which inspire us... to give you some indication of our preferred styles, functions and layouts:

http://www.frostmeridian.example/en/ (we really like this, great personality, like the use of icons for tour types)
http://www.pebblewalks.example.uk/ (very simple design elements and layout)
http://www.sunvalecoast.example/ (great use of background image, nice simple nav bar)
http://www.roamcedarfall.example/ (we like because it has distinct personality and is well suited to the destination)
http://www.seemarlowton.example/ (clear personality through font use)
http://www.vastroving.example/ (original, unique)
http://www.wanderquill.example/long-loop-of-asia (like the map style)

Key design points:

1. You must use our existing logo (attached), but you can change the color scheme of the logo to accord with the whichever color scheme you choose for the main designs.
2. Our logo strapline is "Asia is our Lanternpath" and should be used prominently on the page to reinforce the meaning of our company name.
3. Home page and tours list pages should allow the user to see the choice of tours immediately without scrolling & Introduction copy should be minimal.
4. We and our site visitors are inspired and excited by our photography, this is an element of the site which we would like to maintain and build on, though the section page header sliders are currently too big and do not allow quick access to the section content. This is a design problem which needs a solution. Full page photographic backgrounds may be an answer?
5. Tour page should display other contextual tours, from the same country or style/type
6. We should promote press coverage in various places
7. We should display consultant profiles in various places
8. Map designs for tour page and country page, plus a modal pop out for the home page. These are complex and may have a few small photos and short descriptive text only, though this is limited by your own creativity. We will use graphics and html5/css3 so there are no creative limitations.
9. The 'Inspirations' / 'Be Inspired' page is for people who want travel and holiday ideas, who are looking for inspiration on where to go and what to do. This section needs to reflect the exotic, the unusual, the extraordinary in our destinations and tours, and we leave this to your creative genius to develop. We are also interested in how this inspirations page is related to the blog and social media content we produce daily, is there an integration here? Can we present YouTube videos, our blog posts, Circlewall posts etc, on this page? This is another design challenge.
10. We would like to see designs for the tours list page which feature AJAX content filtering (for instance: http://demo.layoutbrisk.example/?acn), we would like to see how to include this type of content filtering on homepage and destination page also.
11. The 'Enquiry' call to action should be on all pages and prominent.
12. The enquiry page can reflect the same fields as the existing website enquiry page

Values to be communicated:

- Exotic: Asia is exotic, and our tours will expose clients to extraordinary sights and unusual cultural encounters.
- Authentic: Our travel consultants all live in the destinations themselves, they are local nationals and have all the insider knowledge to give clients a truly authentic experience of our destinations
- Unique: All of our tours are tailor made, there are no fixed departure dates or join-in groups. All tour itineraries can be uniquely designed for our clients, from departure dates to destinations.
- Trust: Some travelers prefer to book their holidays with local agencies they can meet in person, rather than with online companies like us who live in the destinations and who they only get to meet on Skype video or phone. We want to convey that we are trustworthy. We have attempted this through presenting a 'meet the team' page and a 'press' page and advert, as well as offering a prominent international phone number. How we you build on this and further convey this value?

```html
<!DOCTYPE html>
<html lang="en">
<head>
<meta charset="utf-8">
<title>Lanternpath Journeys</title>
<link href="https://fonts.googleapis.com/css2?family=Open+Sans:wght@400;600;700&family=Roboto+Condensed:wght@400;700&display=swap" rel="stylesheet">
<style>
:root{
  --orange:#e8731a;
  --blue:#1a6fb5;
  --blue-dark:#12558f;
  --ink:#333;
  --muted:#666;
  --line:#d8d8d8;
  --page:#efefef;
  --footer:#1c2028;
  --footer-bottom:#14171d;
  --footer-head:#e3a12f;
}
*{margin:0;padding:0;box-sizing:border-box}
html,body{width:682px;height:1200px;overflow:hidden}
body{position:relative;background:var(--page);font-family:"Open Sans",sans-serif;color:var(--ink);font-size:6px}
.abs{position:absolute}
.cond{font-family:"Roboto Condensed",sans-serif}

/* header */
.brand{left:80px;top:28px;width:162px;height:54px;background:#fff;box-shadow:0 1px 3px rgba(0,0,0,.2);display:flex;align-items:center;padding-left:12px;gap:7px}
.brand-mark{width:18px;height:18px;border-radius:50%;background:var(--blue)}
.brand-name{font-size:11px;font-weight:700;color:var(--blue);line-height:1.1}
.brand-name small{display:block;font-size:6px}
.callbox{left:466px;top:10px;width:136px;height:34px;background:#fff;border:1px solid #ddd;padding:3px 0 0 40px}
.callbox .ico{position:absolute;left:8px;top:6px;width:22px;height:22px;border-radius:50%;background:#d9d2c8}
.callbox .l1{font-size:8px;color:#555}
.callbox .num{font-size:11px;font-weight:700;color:var(--orange);line-height:1.1}
.callbox .l3{font-size:5px;color:#666}
.nav{left:263px;top:56px;display:flex;align-items:center;font-size:7px;font-weight:600;color:#444}
.nav .home{width:12px;height:12px;border-radius:50%;background:#ddd;margin-right:8px;display:flex;align-items:center;justify-content:center}
.nav span.item{padding:0 7px;border-left:1px solid #bbb}
.nav span.item:first-of-type{border-left:0}

/* hero */
.hero{left:0;top:74px;width:682px;height:256px;background:linear-gradient(180deg,#8a7a5e 0%,#c9a45a 35%,#a87a2f 65%,#5a3c1c 100%)}
.search{left:422px;top:77px;width:180px;height:26px}
.search .bar{height:14px;background:#fff;display:flex;align-items:center;padding-left:3px;font-size:5.5px;color:#333}
.search .field{margin-left:6px;width:124px;height:10px;border:1px solid #ccc}
.search .more{height:11px;background:#6e7f8c;color:#fff;font-size:5px;padding:2px 3px}
.caption{left:430px;top:218px;width:172px;height:53px;background:#fff;border:1px solid var(--orange);padding:6px 8px}
.caption h2{font-family:"Roboto Condensed",sans-serif;font-size:15px;font-weight:700;color:#222;line-height:1}
.caption .sub{font-size:6.5px;font-weight:600;color:var(--orange);margin-top:4px}
.caption .more{font-size:7px;color:#444;margin-top:3px}

/* carousel */
.things{left:80px;top:310px;width:522px;height:148px;background:#fff;box-shadow:0 1px 3px rgba(0,0,0,.15)}
.things-bar{left:80px;top:310px;width:522px;height:20px;background:#f2f2f2;border-bottom:1px solid #ddd;font-family:"Roboto Condensed",sans-serif;font-size:12px;color:#444;padding:2px 8px}
.dest{top:343px;width:120px;height:95px}
.dest .label{position:absolute;left:0;bottom:0;width:100%;height:15px;background:var(--blue);color:#fff;font-weight:700;font-size:7.5px;padding:3px 7px}
.arrow{top:378px;width:18px;height:18px;border-radius:50%;background:#fff;border:1px solid #ccc;display:flex;align-items:center;justify-content:center}

/* intro */
.intro-title{left:80px;top:472px;font-family:"Roboto Condensed",sans-serif;font-size:13px;color:var(--orange)}
.video{left:82px;top:495px;width:144px;height:107px;background:linear-gradient(160deg,#8db1d8,#c74a3c 60%,#3a3a3a);border:2px solid #fff;box-shadow:0 0 2px rgba(0,0,0,.3)}
.video .ctrl{position:absolute;left:0;bottom:0;width:100%;height:10px;background:#222}
.video .play{position:absolute;left:55px;top:40px;width:26px;height:20px;background:#d42;border-radius:3px}
.intro-text{left:236px;top:495px;width:200px;font-size:6px;line-height:9.6px;color:#444}
.intro-text p{margin-bottom:3px}
.intro-text .cta{color:var(--orange);font-weight:700}

/* side panels */
.panel{background:#fff;border:1px solid #ddd}
.panel-head{background:var(--blue);color:#fff;font-family:"Roboto Condensed",sans-serif;font-size:11px;padding:2px 6px;height:17px}
.blog{left:448px;top:474px;width:154px;height:134px}
.blog .date{position:absolute;left:5px;top:26px;width:20px;height:24px;border:1px solid #ccc;border-radius:2px;text-align:center;font-size:7px;font-weight:700;line-height:1.1;padding-top:3px}
.blog .body{position:absolute;left:34px;top:26px;width:114px;font-size:5.8px;line-height:11.3px;color:#555}
.blog .body b{color:#333}
.pill{position:absolute;height:12px;border-radius:6px;background:#eee;border:1px solid #ccc;font-size:6px;padding:2px 16px 0 9px;color:#333}
.pill::after{content:"";position:absolute;right:2px;top:1.5px;width:8px;height:8px;border-radius:50%;background:var(--blue)}

/* tours */
.tour{width:171px;height:181px;background:#fff;border:1px solid #ddd}
.tour .img{height:85px;display:flex;align-items:center;justify-content:center;text-align:center;color:#fff;font-family:"Roboto Condensed",sans-serif;font-weight:700;font-size:10px;line-height:13px;position:relative}
.tour .seal{position:absolute;right:4px;bottom:-3px;width:24px;height:24px;border-radius:50%;background:#f4ede0;border:2px solid #fff}
.tour .seal.red{background:#d22}
.tour .rows{padding:5px 7px;font-size:6.5px;position:relative;height:74px}
.tour .lbl{position:absolute;left:7px;color:#333;font-weight:600;font-size:6.5px}
.tour .val{position:absolute;left:86px;font-size:6.3px;color:#444}
.tour .price{color:var(--orange);font-size:7px}
.tour .facts{position:absolute;left:7px;top:55px;width:156px;font-size:5.6px;line-height:8px;color:#555}
.tour .foot{position:absolute;left:0;bottom:0;width:100%;height:22px;background:#f3f3f3;border-top:1px solid #e2e2e2;font-size:5.8px;color:#444;padding:6px 8px}
.tour .foot .box{display:inline-block;width:8px;height:7px;border:1px solid #aaa;margin-left:4px;vertical-align:-1px;background:#fff}
.tour .btn{position:absolute;right:8px;top:4px;width:49px;height:14px;background:var(--orange);color:#fff;font-size:6.3px;text-align:center;padding-top:3px;border-radius:1px}

/* social widget */
.social{left:448px;top:624px;width:154px;height:154px}
.social .inner{position:absolute;left:5px;top:5px;width:142px;height:143px;border:1px solid #8aa0c8}
.social .head{height:22px;background:#3b5b98;color:#fff;font-size:9px;font-weight:700;padding:5px 5px}
.social .head small{position:absolute;right:4px;top:8px;font-size:4.3px;font-weight:400}
.social .name{position:absolute;left:8px;top:28px;font-size:6.5px;font-weight:700;color:var(--blue)}
.social .like{position:absolute;right:5px;top:28px;width:22px;height:10px;border:1px solid #ccc;font-size:5px;text-align:center;padding-top:1px;color:#3b5b98}
.fan{position:absolute;width:26px;height:26px;background:#9a8f86}
.fan + span{position:absolute;font-size:4.5px;color:#666}
.social .plug{position:absolute;left:8px;top:131px;font-size:4.5px;color:#555}
.social .join{position:absolute;right:8px;top:129px;font-size:7px;font-weight:700;color:#3b5b98}

/* why */
.why{left:448px;top:798px;width:154px;height:154px;overflow:hidden}
.why ul{list-style:none;padding:7px 8px 0 8px}
.why li{position:relative;padding-left:10px;font-size:6px;line-height:8.6px;color:#444;margin-bottom:6px}
.why li::before{content:"";position:absolute;left:0;top:2px;width:5px;height:5px;border-radius:50%;background:#e9b329}
.why .scene{position:absolute;left:0;bottom:0;width:100%;height:64px;background:linear-gradient(180deg,#fff 0%,#c9d8ee 35%,#7d9ac4 80%,#3f5674 100%)}

/* tweet band */
.tweet{left:0;top:1008px;width:682px;height:50px;background:#fff;border-top:1px solid #ddd}
.tweet .bird{position:absolute;left:94px;top:18px;width:10px;height:10px;border-radius:50%;background:var(--blue)}
.tweet .t{position:absolute;left:111px;top:19px;font-size:7.5px;font-weight:700;color:var(--blue)}
.tweet .msg{position:absolute;left:175px;top:20px;font-size:6.5px;color:#555}
.tweet .follow{position:absolute;left:455px;top:20px;font-size:7.5px;font-weight:700;color:var(--blue)}
.tweet .sq{position:absolute;top:17px;width:13px;height:13px;border-radius:2px}

/* footer */
.footer{left:0;top:1058px;width:682px;height:120px;background:var(--footer);color:#ccc}
.fcol{position:absolute;top:13px}
.fcol h4{font-family:"Roboto Condensed",sans-serif;font-size:7.5px;color:var(--footer-head);font-weight:700;margin-bottom:6px;letter-spacing:.2px}
.fcol a{display:block;color:#ccc;font-size:6px;line-height:11px;text-decoration:none}
.fcol p{font-size:5.6px;line-height:11px;width:136px}
.email{margin-top:6px;width:132px;height:20px;display:flex}
.email .in{flex:1;background:#fff;font-size:5.6px;font-style:italic;color:#666;padding:6px 5px}
.email .go{width:20px;background:#5b6c7a;display:flex;align-items:center;justify-content:center}
.find{display:flex;align-items:center;gap:8px;font-size:7px;line-height:15px}
.find i{width:8px;height:8px;background:#6d737e;border-radius:2px;display:inline-block}
.fbottom{left:0;top:1178px;width:682px;height:22px;background:var(--footer-bottom);color:#bbb;font-size:5.5px;padding:7px 81px;display:flex;justify-content:space-between}
</style>
</head>
<body>

<!-- header -->
<div class="abs brand">
  <span class="brand-mark"></span>
  <span class="brand-name">Lanternpath Journeys<small>Asia is our Lanternpath</small></span>
</div>
<div class="abs callbox">
  <span class="ico" role="img" aria-label="Travel consultant with headset"></span>
  <div class="l1">Call toll free</div>
  <div class="num">+800-4417-3860</div>
  <div class="l3">+(INTERNATIONAL DIAL CODE)</div>
</div>
<nav class="abs nav">
  <span class="home"><svg width="7" height="7" viewBox="0 0 10 10"><path d="M1 5L5 1l4 4H8v4H6V6H4v3H2V5z" fill="#555"/></svg></span>
  <span class="item">DESTINATIONS</span><span class="item">TOURS</span><span class="item">HOLIDAY TYPES</span><span class="item">BEST VALUE</span><span class="item">ABOUT US</span><span class="item">BLOG</span>
</nav>

<!-- hero -->
<div class="abs hero" role="img" aria-label="Golden pagoda and temple spires at dusk in Myanmar"></div>
<div class="abs search">
  <div class="bar">SEARCH <span class="field"></span>
    <svg width="8" height="8" viewBox="0 0 10 10" style="margin-left:3px"><circle cx="4" cy="4" r="3" stroke="#333" stroke-width="1.4" fill="none"/><path d="M6 6l3 3" stroke="#333" stroke-width="1.4"/></svg></div>
  <div class="more">SEARCH FOR MORE <span style="color:#f0a020">▾</span></div>
</div>
<div class="abs caption">
  <h2>THE BEST OF MYANMAR</h2>
  <div class="sub">Myanmar — sitting on the cusp of change</div>
  <div class="more">Find out more</div>
</div>

<!-- things to see -->
<div class="abs things"></div>
<div class="abs things-bar">Things to see and do in Asia
  <svg width="12" height="14" viewBox="0 0 12 14" style="position:absolute;left:146px;top:6px"><path d="M8 1c2 4 0 8-4 10M2 8l2 3 3-1" stroke="var(--orange)" stroke-width="1.2" fill="none"/></svg>
</div>
<div class="abs dest" style="left:94px;background:linear-gradient(180deg,#6fa0d0,#e6eef4 45%,#6d8a4a)" role="img" aria-label="Great Wall winding over misty mountains"><span class="label">EPIC CHINA</span></div>
<div class="abs dest" style="left:219px;background:linear-gradient(180deg,#d9cbb0,#9a8766 50%,#6e5c40)" role="img" aria-label="Junk boat among limestone karsts"><span class="label">VIETNAM</span></div>
<div class="abs dest" style="left:345px;background:linear-gradient(160deg,#6d7a55,#b89a6a 45%,#5a4a36)" role="img" aria-label="Floating market vendor with produce"><span class="label">THAILAND</span></div>
<div class="abs dest" style="left:470px;background:linear-gradient(180deg,#7d7560,#5f5842 50%,#3e3a2c)" role="img" aria-label="Carved stone temple reliefs"><span class="label">CAMBODIA</span></div>
<div class="abs arrow" style="left:70px"><svg width="6" height="8" viewBox="0 0 6 8"><path d="M5 1L1 4l4 3" stroke="#333" stroke-width="1.4" fill="none"/></svg></div>
<div class="abs arrow" style="left:595px"><svg width="6" height="8" viewBox="0 0 6 8"><path d="M1 1l4 3-4 3" stroke="#333" stroke-width="1.4" fill="none"/></svg></div>

<!-- intro -->
<h1 class="abs intro-title">ASIA IS OUR LANTERNPATH</h1>
<div class="abs video" role="img" aria-label="Video still of a dragon dance festival">
  <span class="play"><svg width="26" height="20" viewBox="0 0 26 20"><path d="M10 5l8 5-8 5z" fill="#fff"/></svg></span>
  <span class="ctrl"></span>
</div>
<div class="abs intro-text">
  <p>No one knows a destination better than someone who lives, works and plays there. That's the foundation of Lanternpath Journeys. Our travel specialists reside in Asia. They live Asia, they breathe Asia. And they're intrigued explorers as much as they are citizens of Bangkok, or Bali, or Luang Prabang.</p>
  <p>The result is a travel company tailor-made for the person with a taste for veering off the well-trodden path, for the adventurer who wants access to Asia's most spectacular sights, but hidden charms as well, on the road less traveled.</p>
  <p class="cta">Want to explore this Asia? Step into our Lanternpath. »</p>
</div>

<!-- latest blogpost -->
<div class="abs panel blog">
  <div class="panel-head">Latest Blogpost</div>
  <div class="date">1<br>AUG</div>
  <div class="body"><b>Lorem ipsum dolor sit amet</b><br>Facilisis at vero eros et accumsan et iusto odio dignissim blandit praesent luptatum delenit augue duis dolore te feugait null facilisi.consectetuer.Ut wisi enim ad minim veniam, nostrud exerci tation ullamcorper sus lobortis</div>
  <span class="pill" style="left:87px;top:115px">Visit Blog</span>
</div>

<!-- tours -->
<div class="abs tour" style="left:80px;top:624px">
  <div class="img" style="background:linear-gradient(180deg,#b4501c,#7a2e10)" role="img" aria-label="Warm-lit temple interior in Mandalay">A TALE OF TWO CITIES:<br>MANDALAY TO BAGAN<span class="seal"></span></div>
  <div class="rows">
    <span class="lbl" style="top:5px">PROMOTION PRICE</span><span class="val price" style="top:5px">$624 (10% Off)</span><span class="val" style="top:14px;font-size:5.5px">Price Per Person</span>
    <span class="lbl" style="top:28px">DURATION</span><span class="val" style="top:28px">4 DAYS / 3 NIGHTS</span>
    <span class="lbl" style="top:40px">FAST FACTS</span>
    <span class="facts">Romantic in name &amp; alluring in nature, experience 2 of Myanmar's finest; Mandalay &amp; Bagan.</span>
  </div>
  <div class="foot">Send an Inquiry<span class="box"></span><span class="btn">View Tour +</span></div>
</div>
<div class="abs tour" style="left:266px;top:624px">
  <div class="img" style="background:linear-gradient(180deg,#4a4a40,#8d8a76 50%,#3c3a30)" role="img" aria-label="Tree roots over Angkor temple ruins">ANCIENT EMPIRE:<br>EXPLORE ANGKOR<span class="seal red"></span></div>
  <div class="rows">
    <span class="lbl" style="top:5px">PROMOTION PRICE</span><span class="val price" style="top:5px">$315 (15% Off)</span><span class="val" style="top:14px;font-size:5.5px">Price Per Person</span>
    <span class="lbl" style="top:28px">DURATION</span><span class="val" style="top:28px">4 DAYS / 3 NIGHTS</span>
    <span class="lbl" style="top:40px">FAST FACTS</span>
    <span class="facts">You've heard of the Angkor temples; now discover &amp; explore these amazing Cambodian relics!</span>
  </div>
  <div class="foot">Send an Inquiry<span class="box"></span><span class="btn">View Tour +</span></div>
</div>
<div class="abs tour" style="left:80px;top:815px">
  <div class="img" style="background:linear-gradient(180deg,#6a3818,#b08030 50%,#5a3010)" role="img" aria-label="Gilded roofs of a Bangkok temple">DISCOVER BANGKOK &amp;<br>ANGKOR WAT</div>
  <div class="rows">
    <span class="lbl" style="top:5px">PROMOTION PRICE</span><span class="val price" style="top:5px">$624 (10% Off)</span><span class="val" style="top:14px;font-size:5.5px">Price Per Person</span>
    <span class="lbl" style="top:28px">DURATION</span><span class="val" style="top:28px">4 DAYS / 3 NIGHTS</span>
    <span class="lbl" style="top:40px">FAST FACTS</span>
    <span class="facts">Romantic in name &amp; alluring in nature, experience 2 of Myanmar's finest; Mandalay &amp; Bagan.</span>
  </div>
  <div class="foot">Send an Inquiry<span class="box"></span><span class="btn">View Tour +</span></div>
</div>
<div class="abs tour" style="left:266px;top:815px">
  <div class="img" style="background:linear-gradient(180deg,#555,#8c8c8c 40%,#7a2a20)" role="img" aria-label="Red palace roofs under a stormy Beijing sky">BEIJING AT A<br>GLANCE<span class="seal"></span></div>
  <div class="rows">
    <span class="lbl" style="top:5px">PROMOTION PRICE</span><span class="val price" style="top:5px">$624 (10% Off)</span><span class="val" style="top:14px;font-size:5.5px">Price Per Person</span>
    <span class="lbl" style="top:28px">DURATION</span><span class="val" style="top:28px">4 DAYS / 3 NIGHTS</span>
    <span class="lbl" style="top:40px">FAST FACTS</span>
    <span class="facts">Romantic in name &amp; alluring in nature, experience 2 of Myanmar's finest; Mandalay &amp; Bagan.</span>
  </div>
  <div class="foot">Send an Inquiry<span class="box"></span><span class="btn">View Tour +</span></div>
</div>

<!-- social widget -->
<div class="abs panel social">
  <div class="inner">
    <div class="head">Circlewall<small>108 people like Lanternpath Journeys</small></div>
    <span class="name">Lanternpath Journeys</span>
    <span class="like">Like</span>
    <span class="fan" style="left:11px;top:45px" role="img" aria-label="Follower avatar"></span><span style="left:18px;top:73px">Nira</span>
    <span class="fan" style="left:43px;top:45px" role="img" aria-label="Follower avatar"></span><span style="left:49px;top:73px">Tavin</span>
    <span class="fan" style="left:75px;top:45px" role="img" aria-label="Follower avatar"></span><span style="left:82px;top:73px">Nira</span>
    <span class="fan" style="left:107px;top:45px" role="img" aria-label="Follower avatar"></span><span style="left:113px;top:73px">Tavin</span>
    <span class="fan" style="left:11px;top:82px" role="img" aria-label="Follower avatar"></span><span style="left:18px;top:110px">Nira</span>
    <span class="fan" style="left:43px;top:82px" role="img" aria-label="Follower avatar"></span><span style="left:49px;top:110px">Tavin</span>
    <span class="fan" style="left:75px;top:82px" role="img" aria-label="Follower avatar"></span><span style="left:82px;top:110px">Nira</span>
    <span class="fan" style="left:107px;top:82px" role="img" aria-label="Follower avatar"></span><span style="left:113px;top:110px">Tavin</span>
    <span class="plug">Circlewall social plugin</span>
    <span class="join">Join Us!</span>
  </div>
</div>

<!-- why -->
<div class="abs panel why">
  <div class="panel-head">Why Lanternpath Journeys?</div>
  <ul>
    <li>We have offices in all our destinations in Asia, open all year-round</li>
    <li>Our Experienced Travel Specialists possess years of knowledge</li>
    <li>You're booking direct,allowing you to save on your holiday</li>
  </ul>
  <div class="scene" role="img" aria-label="Tiered pagoda by a lake under blue sky"></div>
  <span class="pill" style="left:87px;top:133px">Read more</span>
</div>

<!-- tweet band -->
<div class="abs tweet">
  <span class="bird"></span>
  <span class="t">LATEST TWEET</span>
  <span class="msg">Roads Less Travelled - Ghosts of kingdoms past in #Cambodia</span>
  <span class="follow">Follow Us</span>
  <span class="sq" style="left:502px;background:#3b5b98"></span>
  <span class="sq" style="left:519px;background:#4aa3d8"></span>
  <span class="sq" style="left:536px;background:#c8232c"></span>
  <span class="sq" style="left:552px;background:#5a4636"></span>
  <span class="sq" style="left:568px;width:20px;background:#2a6cc0"></span>
</div>

<!-- footer -->
<footer class="abs footer">
  <div class="fcol" style="left:81px"><h4>QUICK LINKS</h4><a>Home</a><a>Destinations</a><a>Tours</a><a>Hotels</a><a>Holiday Types</a><a>Best Value</a><a>Blog</a><a>Contact Us</a></div>
  <div class="fcol" style="left:143px"><h4>OUR LANTERNPATH</h4><a>Thailand</a><a>Vietnam</a><a>Laos</a><a>Cambodia</a><a>Indonesia</a><a>Myanmar</a><a>Japan</a><a>China</a></div>
  <div class="fcol" style="left:216px"><h4>ABOUT LANTERNPATH</h4><a>Why Book With Us</a><a>About Us</a><a>Meet The Team</a><a>Careers</a><a>In The Press</a><a>Affiliate Program</a></div>
  <div class="fcol" style="left:305px"><h4>UBSCRIBE TO OUR E-NEWSLETTER</h4>
    <p>Sign up for Lanternpath Journeys's e-newsletter featuring promotions, travel musings and insider destination.</p>
    <div class="email"><span class="in">Enter your email</span><span class="go"><svg width="6" height="8" viewBox="0 0 6 8"><path d="M1 1l4 3-4 3" stroke="#fff" stroke-width="1.4" fill="none"/></svg></span></div>
  </div>
  <div class="fcol" style="left:459px"><h4>FIND US</h4>
    <div class="find"><i></i>0198 765 432</div>
    <div class="find"><i></i>0198 765 432</div>
    <div class="find"><i></i><span style="text-decoration:underline">info@lanternpathjourneys.example</span></div>
    <div class="find"><i></i>Book A Trip</div>
  </div>
</footer>
<div class="abs fbottom"><span>Copyright © 2013, Lanternpath Journeys | All Rights Reserved</span><span>Terms of use &nbsp;|&nbsp; Privacy Policy</span></div>

</body>
</html>
```